Income Tax Flyer - Updates Needed

Just need to update this flyer design and give it a new look. We would like to keep all the same wording but make it stand out a little more. Our selling point is the "Same Day Tax Advance up to $6,000"

Industry/Entity Type

Lending, Small Loans, Tax Services, Title Loans, Personal Loans

```html
<!DOCTYPE html>
<html lang="en">
<head>
<meta charset="utf-8">
<title>Harborline Financial Group – Tax Advance Flyer</title>
<link href="https://fonts.googleapis.com/css2?family=Poppins:wght@400;500;600;700&display=swap" rel="stylesheet">
<style>
  :root {
    --green: #0b4b2a;
    --green-dark: #073d21;
    --red: #c4232b;
    --paper: #e9e9ea;
    --paper-light: #f2f2f3;
    --ink: #1d1d1f;
    --white: #ffffff;
    --stage: #4a4a4a;
  }
  * { margin: 0; padding: 0; box-sizing: border-box; }
  html, body {
    width: 905px; height: 1200px; overflow: hidden;
    background: var(--stage);
    font-family: "Poppins", sans-serif;
  }
  .flyer {
    position: absolute; left: 31px; top: 0;
    width: 842px; height: 1200px; overflow: hidden;
    background: linear-gradient(160deg, var(--paper-light) 0%, var(--paper) 60%, #e3e4e5 100%);
  }
  .hero-photo {
    position: absolute; left: 0; top: 0; width: 842px; height: 610px;
    background:
      radial-gradient(ellipse at 62% 48%, #c9a990 0%, rgba(201,169,144,0) 38%),
      radial-gradient(ellipse at 22% 60%, #5a4a42 0%, rgba(90,74,66,0) 40%),
      linear-gradient(135deg, #d8d4cc 0%, #b9b2a8 35%, #8ea2b6 60%, #d7c2b6 85%, #cfc8bd 100%);
  }
  .brand {
    position: absolute; left: 35px; top: 70px;
    color: var(--green); font-weight: 600; font-size: 34px; line-height: 1.15;
  }
  .headline {
    position: absolute; left: 38px; top: 518px; width: 658px; height: 151px;
    background: var(--green-dark);
    border-top-right-radius: 58px;
    color: var(--white);
    padding: 10px 0 0 21px;
  }
  .headline-line { display: block; line-height: 1.3; }
  .headline-line--lead { font-size: 45px; font-weight: 600; }
  .headline-line--amount { font-size: 47px; font-weight: 700; margin-top: 2px; letter-spacing: -0.3px; }
  .selling-point {
    position: absolute; left: 38px; top: 673px; width: 658px; height: 51px;
    background: var(--red); color: var(--white);
    font-size: 31px; line-height: 51px; padding-left: 13px; white-space: nowrap;
  }
  .selling-point strong { font-weight: 700; }
  .benefits {
    position: absolute; left: 39px; top: 783px; width: 760px; height: 244px;
    border: 2px solid var(--green); border-radius: 22px;
  }
  .benefits-title {
    position: absolute; left: 0; right: 0; top: -22px; text-align: center;
    color: var(--red); line-height: 1.28;
  }
  .benefits-title-line {
    display: inline-block; background: var(--paper); padding: 0 20px;
    font-size: 31px; font-weight: 400;
  }
  .benefits-title-emphasis { display: block; font-size: 31px; font-weight: 700; }
  .benefit {
    position: absolute; top: 88px; width: 240px; text-align: center;
    color: var(--ink); font-size: 19.5px; line-height: 1.25;
  }
  .benefit-icon { display: block; margin: 0 auto 7px; width: 70px; height: 72px; }
  .benefit--speed { left: 21px; }
  .benefit--amount { left: 279px; }
  .benefit--easy { left: 524px; }
  .benefit-divider {
    position: absolute; top: 84px; width: 2px; height: 132px;
    background: linear-gradient(to bottom, rgba(150,150,150,0), #a9a9a9 50%, rgba(150,150,150,0));
  }
  .footer-shape { position: absolute; left: 0; top: 1075px; width: 842px; height: 125px; }
  .contact-call { position: absolute; left: 24px; top: 1097px; color: var(--white); }
  .contact-call-label { font-size: 24px; font-weight: 400; display: block; line-height: 1.2; }
  .contact-call-number {
    display: flex; align-items: center; gap: 8px;
    font-size: 34px; font-weight: 700; line-height: 1.2; margin-left: -4px;
  }
  .reach { position: absolute; left: 327px; top: 1080px; font-size: 18.5px; line-height: 1.3; color: var(--ink); }
  .reach-email { color: var(--red); font-weight: 700; display: block; }
  .website { position: absolute; left: 582px; top: 1097px; font-size: 21.5px; color: var(--green); }
  .website strong { font-weight: 700; }
  .address {
    position: absolute; left: 329px; top: 1147px; display: flex; align-items: center; gap: 8px;
    color: var(--white); font-size: 17px;
  }
</style>
</head>
<body>
<main class="flyer">
  <div class="hero-photo" role="img" aria-label="Photo of a smiling couple shaking hands with an advisor across an office desk"></div>

  <div class="brand">Harborline<br>Financial Group</div>

  <h1 class="headline">
    <span class="headline-line headline-line--lead">Apply here for</span>
    <span class="headline-line headline-line--amount">$5,000–$6,000 Today!</span>
  </h1>

  <p class="selling-point">Same Day <strong>Tax Advance up to $6,000</strong></p>

  <section class="benefits">
    <h2 class="benefits-title">
      <span class="benefits-title-line">Files your taxes and apply for an</span>
      <span class="benefits-title-emphasis">Easy Advanced!</span>
    </h2>

    <div class="benefit benefit--speed">
      <svg class="benefit-icon" viewBox="0 0 70 72" fill="none" stroke="var(--green)" stroke-width="3" stroke-linecap="round">
        <rect x="28" y="2" width="14" height="6" rx="2"/>
        <line x1="35" y1="8" x2="35" y2="13"/>
        <line x1="55" y1="17" x2="59" y2="13"/>
        <circle cx="35" cy="42" r="28"/>
        <circle cx="35" cy="42" r="20"/>
        <text x="35" y="52" text-anchor="middle" font-family="Poppins, sans-serif" font-weight="700" font-size="26" fill="var(--green)" stroke="none">$</text>
      </svg>
      Available in<br>24 hours or less
    </div>

    <div class="benefit-divider" style="left:270px"></div>

    <div class="benefit benefit--amount">
      <svg class="benefit-icon" viewBox="0 0 70 72" fill="none" stroke="var(--green)" stroke-width="3" stroke-linecap="round" stroke-linejoin="round">
        <path d="M22 52 A26 26 0 1 1 60 30"/>
        <text x="28" y="38" text-anchor="middle" font-family="Poppins, sans-serif" font-weight="700" font-size="20" fill="var(--green)" stroke="none">$</text>
        <path d="M40 56 V32 a4 4 0 0 1 8 0 V46 l10 3 a6 6 0 0 1 4 7 l-3 12 H46 l-9 -10 a4 4 0 0 1 6 -5 z"/>
      </svg>
      Choose your<br>loan amount
    </div>

    <div class="benefit-divider" style="left:542px"></div>

    <div class="benefit benefit--easy">
      <svg class="benefit-icon" viewBox="0 0 70 72" fill="none" stroke="var(--green)" stroke-width="3" stroke-linecap="round" stroke-linejoin="round">
        <rect x="24" y="4" width="36" height="52" rx="3" fill="var(--green)"/>
        <circle cx="42" cy="30" r="9" stroke="var(--white)"/>
        <path d="M8 50 l16 -18 a6 6 0 0 1 9 8 l-5 6 l14 -4 a5 5 0 0 1 3 9 l-20 10 l-6 8 z" fill="var(--paper)"/>
      </svg>
      Quick and<br>Easy
    </div>
  </section>

  <svg class="footer-shape" viewBox="0 0 842 125" aria-hidden="true">
    <path d="M0 2 H240 Q290 2 300 55 L308 125 H0 Z" fill="var(--red)"/>
    <path d="M304 60 H842 V125 H311 Z" fill="var(--green-dark)"/>
  </svg>

  <div class="contact-call">
    <span class="contact-call-label">Contact Us Today!</span>
    <span class="contact-call-number">
      <svg width="30" height="30" viewBox="0 0 30 30" aria-hidden="true">
        <circle cx="15" cy="15" r="14" fill="var(--green-dark)"/>
        <path d="M10 8 l3 0 l1.5 4 l-2 1.5 a9 9 0 0 0 4 4 l1.5 -2 l4 1.5 l0 3 a2 2 0 0 1 -2 2 a13 13 0 0 1 -12 -12 a2 2 0 0 1 2 -2z" fill="var(--white)"/>
      </svg>
      0555 xx xxx
    </span>
  </div>

  <p class="reach">Reach out to us:<span class="reach-email">info@harborline.com</span></p>
  <p class="website">www.<strong>harborline</strong>.com</p>

  <p class="address">
    <svg width="18" height="20" viewBox="0 0 18 20" aria-hidden="true">
      <circle cx="9" cy="9" r="9" fill="var(--white)"/>
      <path d="M9 3.5 a4 4 0 0 1 4 4 c0 3 -4 7 -4 7 s-4 -4 -4 -7 a4 4 0 0 1 4 -4z" fill="var(--red)"/>
      <circle cx="9" cy="7.5" r="1.5" fill="var(--white)"/>
    </svg>
    Address to come:
  </p>
</main>
</body>
</html>
```